design an app for runners to engage them in collective challenges

Creative Brief: Running Application - Collective Challenges
Objective
To design a simple yet impactful mobile application for runners, centered around collective challenges. The app should offer an engaging, user-friendly experience while encouraging participation in running challenges. Starting with a minimalist and robust version, the design must focus on essential features, allowing for future enhancements as the user base grows.

Target Audience
Primary Users: Casual to dedicated runners who enjoy tracking their progress and participating in challenges.
Motivations: Community-driven goals, personal achievements, and tangible rewards.
Needs: A visually appealing, straightforward interface with real-time progress tracking and clear challenge objectives.
Core Features
Main Screen: Current Challenge

Displays the active challenge with a title, visual, prize description, and countdown for kilometers remaining.
Prominent “Join” button for easy participation.
Quick access to challenge conditions (eg, most kilometers, fastest pace, random draw).
Challenge Details

Includes challenge rules, detailed prize information, and victory conditions.
Simplified text for clarity and engagement.
Past Challenges

Showcases previous challenges, total kilometers achieved, and winners.
Admin Section

Enables challenge creation with scheduling, descriptions, and victory criteria.
Minimalist design for ease of use.
Look and Feel
Visual Identity: Clean, modern, and energetic design reflecting the spirit of running and collective achievement.
Color Palette:
Vibrant primary colors: Blue and green for energy and motivation.
Accent colors: Orange or yellow for highlights, paired with a dark background for strong contrast.
Typography:
Sans-serif fonts like Lato or Montserrat for readability.
Bold, prominent numbers for key statistics like kilometers completed.
Icons and Graphics:
Minimalistic icons with light, functional animations (eg, a moving kilometer counter).
Clear, motivational visuals to support collective progress.
Tone and Style
Tone: Encouraging, community-focused, and goal-oriented.
Style: Minimalistic with a focus on clarity and user engagement.
References
Inspirations:
Velta Stride Circle for its simplicity and modern interface.
Quorvo for its community features and tracking precision.
Deliverables
Wireframes and UI designs for all key screens: login, current challenge, challenge details, past challenges, and admin panel.
Visual assets: icons, buttons, and animations.
A consistent design system to ensure scalability for future features.
Updates

Target Market(s)

Casual to dedicated runners who enjoy tracking their progress and participating in challenges.

Industry/Entity Type

sport

Font styles to use
Sans Serif

Colors

Designer to choose colors to be used in the design.

Requirements
Must have
• to design all screens

```html
<!DOCTYPE html>
<html lang="en">
<head>
<meta charset="utf-8">
<title>Velta Stride Circle – Collective Running Challenges</title>
<link href="https://fonts.googleapis.com/css2?family=Montserrat:wght@400;500;600;700;800&display=swap" rel="stylesheet">
<style>
:root{
  --backdrop:#f76b7e;
  --brand:#ea3e58;
  --brand-soft:#f3687c;
  --brand-light:#f88a9a;
  --brand-deep:#d92f4a;
  --orange:#ff8a1e;
  --orange-red:#f0504a;
  --screen-grey:#e6e6e6;
  --field:#ececec;
  --row-pink:#ecc3ca;
  --ink:#1d1d1f;
  --ink-soft:#555;
  --muted:#8a8a8a;
  --white:#fff;
  --gold:#f5b82e;
  --green:#9ccc2b;
}
*{box-sizing:border-box;margin:0;padding:0}
html,body{width:1200px;height:1200px;overflow:hidden;background:var(--backdrop)}
body{font-family:"Montserrat",sans-serif;color:var(--ink)}
.stage{position:absolute;left:0;top:0;width:1920px;height:1920px;transform:scale(.625);transform-origin:0 0}
.screen{position:absolute;width:348px;height:758px;border-radius:44px;overflow:hidden;background:var(--white);box-shadow:0 20px 40px rgba(120,30,45,.28)}
.screen--grey{background:var(--screen-grey)}
.a{position:absolute}
.icon{width:1em;height:1em;fill:currentColor}

/* header */
.avatar{position:absolute;width:44px;height:44px;border-radius:50%;background:var(--brand-soft);color:#fff;font-weight:700;font-size:14px;display:flex;align-items:center;justify-content:center}
.greet small{display:block;font-size:11px;font-weight:500}
.greet b{display:block;font-size:13.5px;font-weight:700;margin-top:-1px}
.bell{font-size:26px;color:var(--ink)}

/* section labels */
.label{font-size:12px;font-weight:700}
.label--lg{font-size:13.5px;font-weight:700}

/* hero */
.hero{border-radius:10px;background:linear-gradient(180deg,var(--brand) 0%,var(--brand-soft) 100%);overflow:hidden;color:#fff;text-align:center}
.hero::before{content:"";position:absolute;width:300px;height:300px;border-radius:50%;right:-110px;top:-110px;background:rgba(255,255,255,.12)}
.hero .runner{position:absolute;left:50%;transform:translateX(-50%);font-size:50px}
.hero .big{position:absolute;left:0;right:0;font-size:34px;font-weight:800;letter-spacing:.5px}
.hero .sub{position:absolute;left:0;right:0;font-size:13px;letter-spacing:2.5px;font-weight:500}
.stat{position:absolute;height:56px;border-radius:8px;background:rgba(255,255,255,.16);color:#fff;text-align:center;padding-top:10px;font-size:13px;line-height:1.25}
.stat span{display:block;font-size:12.5px;opacity:.85}
.stat b{font-weight:600}
.stat--icon{padding-top:6px}
.stat--icon .icon{font-size:13px}
.stat--icon span{font-size:11px}
.stat--icon b{font-size:15px;font-weight:700}

/* challenge card */
.challenge{border-radius:10px;overflow:hidden;background:linear-gradient(180deg,#f3c3cb 0%,#efb2bd 55%,#f4cbd2 100%)}
.challenge .scenery{position:absolute;inset:0;background:linear-gradient(170deg,rgba(255,255,255,.35) 0%,rgba(232,138,154,.35) 60%,rgba(255,255,255,.2) 100%)}
.pill{position:absolute;border-radius:14px;background:var(--brand);color:#fff;font-size:13px;font-weight:500;display:flex;align-items:center;justify-content:center;border:2px solid #fff}
.ch-title{position:absolute;font-size:17px;font-weight:800;color:var(--brand)}
.ch-small{position:absolute;font-size:10.5px;color:#5a3b40}
.bar{position:absolute;height:5px;border-radius:3px;background:rgba(150,150,150,.45);overflow:hidden}
.bar i{position:absolute;left:0;top:0;bottom:0;width:58%;background:linear-gradient(90deg,var(--brand),var(--orange))}
.prize{position:absolute;height:31px;border-radius:5px;background:linear-gradient(90deg,var(--orange) 0%,var(--brand) 45%);color:#fff;font-size:13px;display:flex;align-items:center;padding:0 14px;gap:10px}
.prize--flat{background:var(--brand)}
.prize b{margin-left:auto;font-weight:700}

/* activity rows */
.row{position:absolute;height:42px;border-radius:4px;background:var(--row-pink);padding:5px 0 0 22px}
.row b{display:block;color:var(--brand);font-size:13px;font-weight:500}
.row span{display:block;font-size:10.5px;color:#333}
.row .chev{position:absolute;right:10px;top:13px;font-size:14px;color:var(--brand)}
.award{position:absolute;height:50px;border-radius:4px;background:linear-gradient(90deg,var(--orange) 0%,var(--orange-red) 100%);color:#fff;padding:8px 0 0 17px}
.award b{display:block;font-size:13.5px;font-weight:600}
.award span{display:block;font-size:10.5px;opacity:.9}
.award .icon{position:absolute;right:14px;top:14px;font-size:20px}

/* buttons & nav */
.btn{position:absolute;border-radius:8px;background:linear-gradient(180deg,var(--brand) 0%,#ee5068 100%);color:#fff;font-size:13.5px;display:flex;align-items:center;justify-content:center;box-shadow:0 3px 6px rgba(0,0,0,.15)}
.btn--bold{font-weight:700}
.nav{position:absolute;left:0;right:0;display:flex;justify-content:space-around;padding:0 40px;font-size:22px;color:#9b9b9b}
.nav .on{color:var(--brand)}

/* form */
.field-label{position:absolute;font-size:13.5px;font-weight:600}
.field{position:absolute;height:44px;border:1.5px solid #a9a9a9;border-radius:6px;background:var(--field);font-size:13px;color:var(--muted);padding:0 16px;display:flex;align-items:center}
.field--white{background:#f7f7f7;border-color:#bbb}
.field--area{align-items:flex-start;padding-top:14px}
.dashed{position:absolute;border:1.5px dashed #aaa;border-radius:6px;display:flex;flex-direction:column;align-items:center;justify-content:center;color:var(--muted);font-size:13px}

/* top band */
.band{position:absolute;left:0;right:0;top:0;height:105px;background:var(--brand)}
.band .back{position:absolute;left:25px;top:64px;font-size:18px;color:#fff}
.band .title{position:absolute;left:47px;top:63px;color:#fff;font-size:14px;font-weight:600}
.band .join{position:absolute;top:55px;width:150px;height:31px;border-radius:6px;background:#d5304b;color:#fff;font-size:14px;display:flex;align-items:center;justify-content:center;box-shadow:0 3px 6px rgba(0,0,0,.25)}

.rules{border-radius:8px;background:linear-gradient(90deg,var(--orange) 0%,var(--orange-red) 100%);color:#fff}
.rule{position:absolute;left:56px}
.rule b{display:block;font-size:13.5px;font-weight:600}
.rule span{display:block;font-size:11.5px;margin-top:-1px}
.rule .icon{position:absolute;left:-35px;top:6px;font-size:20px}

.photo{position:absolute;left:0;top:0;width:100%;height:295px;background:linear-gradient(180deg,#c9b3a2 0%,#8d6b55 35%,#4b4340 70%,#2c2a2a 100%)}
</style>
</head>
<body>
<svg width="0" height="0" style="position:absolute">
  <symbol id="i-run" viewBox="0 0 24 24"><circle cx="14.5" cy="3.5" r="2.2"/><path d="M9.5 7.2l4-1.2c.9-.3 1.8.2 2.2 1l1.3 2.8 3 1.2-.8 1.8-3.7-1.5-.9-1.7-1.3 3.6 2.8 2.6-.9 6.2h-2l.7-5.2-3-2.4-1.6 3.7-4.9-.6.3-2 3.3.4 2.9-7.2-1.6.5-1.5 3-1.8-.8z"/></symbol>
  <symbol id="i-bell" viewBox="0 0 24 24"><path d="M12 3a6 6 0 0 0-6 6v4.5L4 17v1h16v-1l-2-3.5V9a6 6 0 0 0-6-6zm0 1.6A4.4 4.4 0 0 1 16.4 9v4.9l1 1.5H6.6l1-1.5V9A4.4 4.4 0 0 1 12 4.6zM10 19.5a2 2 0 0 0 4 0z"/></symbol>
  <symbol id="i-home" viewBox="0 0 24 24"><path d="M12 3L2 12h3v8h5v-5h4v5h5v-8h3z"/></symbol>
  <symbol id="i-trophy" viewBox="0 0 24 24"><path d="M6 3h12v2h3v3a4 4 0 0 1-4 4h-.4A5 5 0 0 1 13 14.8V17h3v3H8v-3h3v-2.2A5 5 0 0 1 7.4 12H7a4 4 0 0 1-4-4V5h3zm0 4H5v1a2 2 0 0 0 1 1.7zm12 0v2.7A2 2 0 0 0 19 8V7z"/></symbol>
  <symbol id="i-history" viewBox="0 0 24 24"><path d="M13 3a9 9 0 0 0-9 9H1l3.9 3.9L8.8 12H6a7 7 0 1 1 2.1 5l-1.4 1.4A9 9 0 1 0 13 3zm-1 5v5l4.3 2.5.7-1.2-3.5-2.1V8z"/></symbol>
  <symbol id="i-user" viewBox="0 0 24 24"><circle cx="12" cy="7.5" r="4.5"/><path d="M3 21c0-4.5 4-7 9-7s9 2.5 9 7z"/></symbol>
  <symbol id="i-medal" viewBox="0 0 24 24"><path d="M5 2h4l3 5 3-5h4l-4.5 7.3A6.5 6.5 0 1 1 9.5 9.3zm7 9a4.5 4.5 0 1 0 0 9 4.5 4.5 0 0 0 0-9zm0 1.8l1.2 2.4 2.6.3-1.9 1.8.5 2.6-2.4-1.3-2.4 1.3.5-2.6-1.9-1.8 2.6-.3z"/></symbol>
  <symbol id="i-ribbon" viewBox="0 0 24 24"><path d="M12 2a7 7 0 0 0-4.5 12.4L6 22l6-3 6 3-1.5-7.6A7 7 0 0 0 12 2zm0 2.5a4.5 4.5 0 1 1 0 9 4.5 4.5 0 0 1 0-9z"/></symbol>
  <symbol id="i-chev" viewBox="0 0 24 24"><path d="M8.6 4.6L10.7 2.5 20.2 12l-9.5 9.5-2.1-2.1L16 12z"/></symbol>
  <symbol id="i-back" viewBox="0 0 24 24"><path d="M20 11H7.8l5.6-5.6L12 4l-8 8 8 8 1.4-1.4L7.8 13H20z"/></symbol>
  <symbol id="i-crown" viewBox="0 0 24 24"><path d="M2 6l5 5 5-7 5 7 5-5-2 13H4zm3.7 11h12.6l1.1-7.5-3 3L12 7.4l-4.4 5.1-3-3z"/></symbol>
  <symbol id="i-users" viewBox="0 0 24 24"><circle cx="12" cy="7" r="3.5"/><circle cx="5" cy="9" r="2.5"/><circle cx="19" cy="9" r="2.5"/><path d="M5 20c0-4 3-6.5 7-6.5s7 2.5 7 6.5zM0 19c0-3 2-5 4.5-5L4 19zM24 19c0-3-2-5-4.5-5l.5 5z"/></symbol>
  <symbol id="i-clock" viewBox="0 0 24 24"><path d="M12 2a10 10 0 1 0 0 20 10 10 0 0 0 0-20zm1 5v5.4l3.8 2.3-1 1.6L11 13.5V7z"/></symbol>
  <symbol id="i-trend" viewBox="0 0 24 24"><path d="M2 17.6L9 10.6l4 4L19.6 8H16V6h7v7h-2V9.4l-8 8-4-4-5.6 5.6z"/></symbol>
  <symbol id="i-cal" viewBox="0 0 24 24"><path d="M7 2h2v2h6V2h2v2h3v18H4V4h3zm-1 7v11h12V9z"/></symbol>
  <symbol id="i-watch" viewBox="0 0 24 24"><path d="M9 1h6v2H9zm3 3a9 9 0 1 0 0 18 9 9 0 0 0 0-18zm-1 4h2v6h-2zm7.4-2.4l1.4-1.4 1.4 1.4-1.4 1.4z"/></symbol>
  <symbol id="i-trash" viewBox="0 0 24 24"><path d="M9 2h6l1 2h5v2H3V4h5zM5 8h14l-1 14H6zm4 2v10h1.6V10zm4.4 0v10H15V10z"/></symbol>
</svg>

<main class="stage">

  <!-- Sign up -->
  <section class="screen screen--grey" style="left:158px;top:112px;background:#dcdcdc">
    <div class="photo" role="img" aria-label="Photo of a runner's legs and shoes on an open desert road with a yellow centre line"></div>
    <h1 class="a" style="left:0;right:0;top:308px;text-align:center;font-size:18px;font-weight:600;color:#333">Create Account</h1>
    <p class="a" style="left:0;right:0;top:338px;text-align:center;font-size:9.5px;color:#444">Join our running community and start tracking your progress</p>
    <label class="field-label" style="left:15px;top:369px">First Name</label>
    <div class="field" style="left:15px;top:394px;width:314px">Lena</div>
    <label class="field-label" style="left:15px;top:447px">Last Name</label>
    <div class="field" style="left:17px;top:471px;width:314px">Marsh</div>
    <label class="field-label" style="left:15px;top:524px">Email</label>
    <div class="field" style="left:17px;top:549px;width:314px">lm@runmail.io</div>
    <label class="field-label" style="left:15px;top:602px">Password</label>
    <div class="field" style="left:17px;top:626px;width:314px">lm@runmail.io</div>
    <div class="btn" style="left:16px;top:680px;width:313px;height:58px">Publish Challenge</div>
  </section>

  <!-- Home: today's progress -->
  <section class="screen screen--grey" style="left:787px;top:105px">
    <div class="avatar" style="left:16px;top:58px">LM</div>
    <div class="a greet" style="left:66px;top:65px"><small>Welcome Back</small><b>Lena M.</b></div>
    <svg class="a icon bell" style="left:302px;top:70px"><use href="#i-bell"/></svg>

    <div class="a hero" style="left:16px;top:121px;width:313px;height:237px">
      <svg class="icon a" style="left:266px;top:16px;font-size:26px;fill:var(--gold)"><use href="#i-crown"/></svg>
      <svg class="icon runner" style="top:33px"><use href="#i-run"/></svg>
      <div class="big" style="top:96px">2.5 km</div>
      <div class="sub" style="top:134px">Today's Progress</div>
      <div class="stat" style="left:12px;top:172px;width:87px"><span>Time</span><b>22 Min</b></div>
      <div class="stat" style="left:113px;top:172px;width:86px"><span>Pace</span><b>8'48" /km</b></div>
      <div class="stat" style="left:214px;top:172px;width:87px"><span>Calories</span><b>186 kcal</b></div>
    </div>

    <div class="a label" style="left:33px;top:377px">Current Challenge</div>
    <div class="a challenge" style="left:16px;top:403px;width:313px;height:149px">
      <div class="scenery" role="img" aria-label="Soft pink mountain and pine forest backdrop"></div>
      <div class="ch-title" style="left:17px;top:12px">100km Challenge</div>
      <div class="ch-small" style="left:17px;top:33px">12 days remaining</div>
      <div class="ch-small" style="left:19px;top:58px">35.8 km completed</div>
      <div class="ch-small" style="right:20px;top:58px">53%</div>
      <div class="bar" style="left:20px;top:72px;width:273px"><i></i></div>
      <div class="prize" style="left:16px;top:105px;width:280px"><svg class="icon"><use href="#i-medal"/></svg>Prize Pool<b>US. 10,000</b></div>
    </div>
    <div class="pill" style="left:246px;top:388px;width:72px;height:30px">Active</div>

    <div class="a label--lg" style="left:33px;top:569px">Recent Activities</div>
    <div class="row" style="left:16px;top:590px;width:313px;height:43px"><b>Today • 6:30 AM</b><span>2.5 km &nbsp;22 min</span><svg class="icon chev"><use href="#i-chev"/></svg></div>
    <div class="btn btn--bold" style="left:16px;top:638px;width:313px;height:57px">Start Run</div>
    <nav class="nav" style="top:716px"><svg class="icon on"><use href="#i-home"/></svg><svg class="icon"><use href="#i-trophy"/></svg><svg class="icon"><use href="#i-history"/></svg><svg class="icon"><use href="#i-user"/></svg></nav>
  </section>

  <!-- Home: challenge summary (two instances) -->
  <section class="screen" style="left:1410px;top:112px">
    <div class="avatar" style="left:18px;top:58px">LM</div>
    <div class="a greet" style="left:68px;top:65px"><small>Welcome Back</small><b>Lena M.</b></div>
    <svg class="a icon bell" style="left:304px;top:69px"><use href="#i-bell"/></svg>
    <div class="a label" style="left:35px;top:129px">Current Challenge</div>
    <div class="a challenge" style="left:18px;top:154px;width:313px;height:150px">
      <div class="scenery" role="img" aria-label="Soft pink mountain and pine forest backdrop"></div>
      <div class="ch-title" style="left:17px;top:12px">100km Challenge</div>
      <div class="ch-small" style="left:17px;top:30px">12 days remaining</div>
      <div class="ch-small" style="left:20px;top:56px">35.8 km completed</div>
      <div class="ch-small" style="right:20px;top:56px">53%</div>
      <div class="bar" style="left:20px;top:71px;width:274px"><i></i></div>
      <div class="prize prize--flat" style="left:17px;top:107px;width:279px"><svg class="icon"><use href="#i-medal"/></svg>Prize Pool<b>US. 10,000</b></div>
    </div>
    <div class="pill" style="left:247px;top:143px;width:65px;height:28px">Active</div>
    <div class="a label--lg" style="left:37px;top:319px">Recent Activities</div>
    <div class="row" style="left:20px;top:347px;width:312px;height:40px"><b>Today • 6:30 AM</b><span>2.5 km &nbsp;22 min</span><svg class="icon chev"><use href="#i-chev"/></svg></div>
    <div class="row" style="left:20px;top:396px;width:312px;height:41px"><b>Yesterday • 6:15 AM</b><span>2.5 km &nbsp;22 min</span><svg class="icon chev"><use href="#i-chev"/></svg></div>
    <div class="a label--lg" style="left:37px;top:449px">Recent Activities</div>
    <div class="award" style="left:20px;top:482px;width:312px"><b>50km Speed Run</b><span>Completed • Won 2nd Place</span><svg class="icon" style="color:var(--green)"><use href="#i-ribbon"/></svg></div>
    <div class="award" style="left:20px;top:539px;width:312px"><b>Marathon Prep</b><span>Completed • Participation</span><svg class="icon"><use href="#i-ribbon"/></svg></div>
    <div class="btn btn--bold" style="left:17px;top:638px;width:312px;height:57px">Start Run</div>
    <nav class="nav" style="top:716px"><svg class="icon on"><use href="#i-home"/></svg><svg class="icon"><use href="#i-trophy"/></svg><svg class="icon"><use href="#i-history"/></svg><svg class="icon"><use href="#i-user"/></svg></nav>
  </section>

  <section class="screen" style="left:158px;top:1062px">
    <div class="avatar" style="left:18px;top:58px">LM</div>
    <div class="a greet" style="left:68px;top:65px"><small>Welcome Back</small><b>Lena M.</b></div>
    <svg class="a icon bell" style="left:304px;top:69px"><use href="#i-bell"/></svg>
    <div class="a label" style="left:35px;top:129px">Current Challenge</div>
    <div class="a challenge" style="left:18px;top:154px;width:313px;height:150px">
      <div class="scenery" role="img" aria-label="Soft pink mountain and pine forest backdrop"></div>
      <div class="ch-title" style="left:17px;top:12px">100km Challenge</div>
      <div class="ch-small" style="left:17px;top:30px">12 days remaining</div>
      <div class="ch-small" style="left:20px;top:56px">35.8 km completed</div>
      <div class="ch-small" style="right:20px;top:56px">53%</div>
      <div class="bar" style="left:20px;top:71px;width:274px"><i></i></div>
      <div class="prize prize--flat" style="left:17px;top:107px;width:279px"><svg class="icon"><use href="#i-medal"/></svg>Prize Pool<b>US. 10,000</b></div>
    </div>
    <div class="pill" style="left:245px;top:143px;width:68px;height:28px">Active</div>
    <div class="a label--lg" style="left:36px;top:319px">Recent Activities</div>
    <div class="row" style="left:18px;top:347px;width:313px;height:41px"><b>Today • 6:30 AM</b><span>2.5 km &nbsp;22 min</span><svg class="icon chev"><use href="#i-chev"/></svg></div>
    <div class="row" style="left:18px;top:396px;width:313px;height:42px"><b>Yesterday • 6:15 AM</b><span>2.5 km &nbsp;22 min</span><svg class="icon chev"><use href="#i-chev"/></svg></div>
    <div class="a label--lg" style="left:36px;top:450px">Recent Activities</div>
    <div class="award" style="left:19px;top:482px;width:312px"><b>50km Speed Run</b><span>Completed • Won 2nd Place</span><svg class="icon" style="color:var(--green)"><use href="#i-ribbon"/></svg></div>
    <div class="award" style="left:19px;top:539px;width:312px"><b>Marathon Prep</b><span>Completed • Participation</span><svg class="icon"><use href="#i-ribbon"/></svg></div>
    <div class="btn btn--bold" style="left:16px;top:638px;width:312px;height:57px">Start Run</div>
    <nav class="nav" style="top:716px"><svg class="icon on"><use href="#i-home"/></svg><svg class="icon"><use href="#i-trophy"/></svg><svg class="icon"><use href="#i-history"/></svg><svg class="icon"><use href="#i-user"/></svg></nav>
  </section>

  <!-- Challenge details -->
  <section class="screen screen--grey" style="left:787px;top:1055px">
    <header class="band">
      <svg class="icon back"><use href="#i-back"/></svg>
      <div class="title">Overall Statistics</div>
      <div class="join" style="left:182px">Join Challenge</div>
    </header>
    <div class="a hero" style="left:16px;top:123px;width:313px;height:236px">
      <div class="pill" style="left:172px;top:9px;width:132px;height:26px;border:0;background:var(--brand-deep)">Active Challenge</div>
      <svg class="icon runner" style="top:40px"><use href="#i-run"/></svg>
      <div class="big" style="top:101px">100 km</div>
      <div class="sub" style="top:139px;font-size:14px;letter-spacing:3.5px">Challenge</div>
      <div class="stat stat--icon" style="left:12px;top:171px;width:87px"><svg class="icon"><use href="#i-users"/></svg><span>Players</span><b>2,458</b></div>
      <div class="stat stat--icon" style="left:113px;top:171px;width:86px"><svg class="icon"><use href="#i-clock"/></svg><span>Days Left</span><b>12</b></div>
      <div class="stat stat--icon" style="left:214px;top:171px;width:87px"><svg class="icon"><use href="#i-trophy"/></svg><span>Prize</span><b>$10,000</b></div>
    </div>
    <div class="a challenge" style="left:16px;top:372px;width:313px;height:125px">
      <div class="scenery" role="img" aria-label="Soft pink mountain and pine forest backdrop"></div>
      <div class="ch-title" style="left:18px;top:10px">Your Progress</div>
      <div class="ch-small" style="left:19px;top:47px">35.8 km completed</div>
      <div class="ch-small" style="right:20px;top:47px">53%</div>
      <div class="bar" style="left:20px;top:61px;width:273px"><i></i></div>
      <div class="a" style="left:19px;top:82px;font-size:13px;line-height:1.2">Time<br><b>48.5h</b></div>
      <div class="a" style="left:125px;top:82px;font-size:13px;line-height:1.2;text-align:center">Speed<br><b>8.5km/h</b></div>
      <div class="a" style="right:20px;top:82px;font-size:13px;line-height:1.2;text-align:right">Rank<br><b>#234</b></div>
    </div>
    <div class="a rules" style="left:16px;top:513px;width:319px;height:132px">
      <div class="rule" style="top:11px"><svg class="icon"><use href="#i-trend"/></svg><b>Complete 100km</b><span>Complete 100km Within challenge period</span></div>
      <div class="rule" style="top:52px"><svg class="icon"><use href="#i-cal"/></svg><b>30 Days Timeline</b><span>Ends Dec 20, 2024</span></div>
      <div class="rule" style="top:92px"><svg class="icon"><use href="#i-watch"/></svg><b>Minimum 2km per run</b><span>Each activity must qualify</span></div>
    </div>
    <div class="prize prize--flat" style="left:16px;top:665px;width:313px;height:40px;border-radius:6px;padding:0 28px 0 22px"><svg class="icon" style="color:var(--green);font-size:18px"><use href="#i-ribbon"/></svg>1st Place<b style="font-weight:500">$5,000</b></div>
    <nav class="nav" style="top:716px"><svg class="icon"><use href="#i-home"/></svg><svg class="icon on"><use href="#i-trophy"/></svg><svg class="icon"><use href="#i-history"/></svg><svg class="icon"><use href="#i-user"/></svg></nav>
  </section>

  <!-- Admin: create challenge -->
  <section class="screen screen--grey" style="left:1410px;top:1062px">
    <header class="band">
      <svg class="icon back"><use href="#i-back"/></svg>
      <div class="title">Create Challenge</div>
      <div class="join" style="left:183px">Join Challenge</div>
    </header>
    <label class="field-label" style="left:17px;top:124px">Your Progress</label>
    <div class="field field--white" style="left:18px;top:148px;width:314px">ex 108 km Challenge</div>
    <label class="field-label" style="left:17px;top:205px">Description</label>
    <div class="field field--white field--area" style="left:18px;top:229px;width:314px;height:95px">Description your Challenge</div>
    <label class="field-label" style="left:17px;top:336px">Upload Banner</label>
    <div class="dashed" style="left:18px;top:360px;width:314px;height:95px"><b style="font-weight:600;font-size:14px;color:#777">Click to upload banner image</b><span style="font-size:12px">Recommended: 1200 x 400px</span></div>
    <label class="field-label" style="left:17px;top:463px">Challenge Duration</label>
    <div class="field field--white" style="left:18px;top:487px;width:314px">Start Date / End Date</div>
    <label class="field-label" style="left:17px;top:539px">Challenge Rules</label>
    <div class="field field--white" style="left:18px;top:563px;width:314px">Enter Rule<svg class="icon" style="margin-left:auto;font-size:18px;color:#555"><use href="#i-trash"/></svg></div>
    <div class="dashed" style="left:18px;top:615px;width:314px;height:43px">+ &nbsp;Add Rule</div>
    <div class="btn" style="left:17px;top:681px;width:313px;height:57px">Publish Challenge</div>
  </section>

</main>
</body>
</html>
```